Fleyer für Rasenroboter-Garage
Zielgruppe
Aluminiumsysteme
Aufgabenstellung
Für ein neues Produkt " Rasenroboter-Garage" einen Fleyer entwerfen. Format DinA4 Vorder und Rückseite. Bilder der Garage sind als Anhang anbei.Es gibt eine Basic Version mit Dach und eine Expert Version mit Dach und Seitenverkleidung. Sogan " Das Zuhause für Ihren Rasenroboter" . Merkmale sind hochertige Materialien, qualitative Verarbeitung, ästhetisches Design,lange Lebensdauer.

```html
<!DOCTYPE html>
<html lang="de">
<head>
<meta charset="utf-8">
<title>Rasenhaus – Das Zuhause für Ihren Rasenroboter</title>
<link href="https://fonts.googleapis.com/css2?family=Exo+2:wght@400;500;600;700&family=Arimo:wght@400;700&display=swap" rel="stylesheet">
<style>
  :root {
    --page-bg: #d9d9d9;
    --black: #0b0b0b;
    --white: #ffffff;
    --paper: #f1f1f1;
    --text: #151515;
    --grass-dark: #2f6a1c;
    --grass-light: #7fb24a;
    --badge-top: #4a4a4a;
    --badge-bottom: #1e1e1e;
    --note-yellow: #f4ea12;
    --logo-green: #7cc242;
  }
  * { box-sizing: border-box; margin: 0; padding: 0; }
  html, body { width: 1000px; height: 1200px; overflow: hidden; }
  body { background: var(--page-bg); font-family: "Arimo", Arial, sans-serif; color: var(--text); }

  .flyer {
    position: absolute; left: 84px; top: 12px;
    width: 832px; height: 1176px;
    background: var(--paper); overflow: hidden;
  }

  .header {
    position: absolute; left: 0; top: 0; width: 100%; height: 154px;
    background: var(--black); color: var(--white);
    font-family: "Exo 2", sans-serif;
  }
  .header__title { position: absolute; left: 52px; top: 36px; font-size: 50px; line-height: 54px; }
  .header__title strong { font-weight: 700; display: block; }
  .header__title span { font-weight: 400; display: block; }

  .brand { position: absolute; right: 44px; top: 54px; display: flex; align-items: center; gap: 10px; }
  .brand__mark { width: 22px; height: 22px; background: var(--logo-green); }
  .brand__name { font-family: "Exo 2", sans-serif; font-weight: 700; font-size: 32px; color: var(--logo-green); }

  .scene {
    position: absolute; left: 0; top: 154px; width: 100%; height: 500px;
    background: linear-gradient(180deg, var(--grass-light) 0%, var(--grass-dark) 55%, #dfe6da 66%, var(--paper) 100%);
  }
  .scene__product {
    position: absolute; left: 60px; top: 195px; width: 420px; height: 290px;
    background: linear-gradient(180deg, #2c4a3c 0%, #1d3128 60%, #c9c9c9 100%);
    border-radius: 4px;
  }

  .features {
    position: absolute; left: 474px; top: 436px; width: 308px;
    background: linear-gradient(160deg, var(--badge-top), var(--badge-bottom));
    color: var(--white); transform: rotate(-4deg);
    box-shadow: 0 6px 14px rgba(0,0,0,.35);
    padding: 18px 20px 20px; font-family: "Exo 2", sans-serif;
  }
  .features__title { font-size: 22px; font-weight: 600; line-height: 26px; margin-bottom: 8px; }
  .features__list { list-style: none; }
  .features__list li { display: flex; align-items: center; gap: 10px; font-size: 19px; line-height: 32px; white-space: nowrap; }
  .features__list svg { width: 13px; height: 13px; flex: none; }

  .claim { position: absolute; left: 52px; top: 684px; font-family: "Exo 2", sans-serif; font-size: 42px; line-height: 54px; }
  .claim span { font-weight: 400; display: block; }
  .claim strong { font-weight: 700; display: block; }

  .copy { position: absolute; left: 52px; top: 818px; width: 500px; font-size: 13.5px; line-height: 18px; }
  .copy p { margin-bottom: 16px; }

  .versions {
    position: absolute; left: 573px; top: 812px; width: 205px; height: 150px;
    background: var(--note-yellow); transform: rotate(-4deg);
    box-shadow: 0 4px 10px rgba(0,0,0,.3);
    padding: 14px 16px; font-size: 13.5px; line-height: 17px;
  }
  .versions strong { display: block; margin-top: 10px; font-family: "Exo 2", sans-serif; font-size: 20px; line-height: 24px; font-weight: 700; }

  .backside-hint {
    position: absolute; left: 596px; top: 996px; transform: rotate(-4deg);
    display: flex; align-items: center; gap: 6px;
    font-family: "Exo 2", sans-serif; font-weight: 700; font-size: 14px; line-height: 15px; text-align: center;
  }
  .backside-hint svg { width: 14px; height: 12px; margin-top: 14px; }

  .contact-cta {
    position: absolute; left: 0; top: 1070px; width: 100%; text-align: center;
    font-family: "Exo 2", sans-serif; font-weight: 700; font-size: 21px;
  }

  .contact-bar {
    position: absolute; left: 0; bottom: 0; width: 100%; height: 60px;
    background: var(--black); color: var(--white);
    font-family: "Exo 2", sans-serif; font-weight: 600; font-size: 26px;
    display: flex; align-items: center; justify-content: center;
  }
</style>
</head>
<body>
  <main class="flyer">
    <header class="header">
      <h1 class="header__title"><strong>Das Zuhause</strong><span>für Ihren Rasenroboter</span></h1>
      <div class="brand"><span class="brand__mark"></span><span class="brand__name">Rasenhaus</span></div>
    </header>

    <div class="scene" role="img" aria-label="Foto: sonnige Rasenfläche im Hintergrund">
      <div class="scene__product" role="img" aria-label="Produktfoto: dunkelgrüne Aluminium-Garage mit Rasenroboter auf seiner Ladestation"></div>
    </div>

    <section class="features">
      <h2 class="features__title">Unsere Box<br>überzeugt durch:</h2>
      <ul class="features__list">
        <li><svg viewBox="0 0 14 14"><path d="M2 7.5l3 3 7-7" fill="none" stroke="#fff" stroke-width="2.4"/></svg>hochwertige Materialien</li>
        <li><svg viewBox="0 0 14 14"><path d="M2 7.5l3 3 7-7" fill="none" stroke="#fff" stroke-width="2.4"/></svg>qualitative Verarbeitung</li>
        <li><svg viewBox="0 0 14 14"><path d="M2 7.5l3 3 7-7" fill="none" stroke="#fff" stroke-width="2.4"/></svg>ästhetisches Design</li>
        <li><svg viewBox="0 0 14 14"><path d="M2 7.5l3 3 7-7" fill="none" stroke="#fff" stroke-width="2.4"/></svg>lange Lebensdauer</li>
      </ul>
    </section>

    <h2 class="claim"><span>Die ideale Ergänzung</span><strong>zu Ihrem Rasenrobotergerät!</strong></h2>

    <div class="copy">
      <p>Die neue Rasenroboter-Garage besticht durch Eleganz. Neben der Werterhaltung Ihres Rasenmähers und dessen Ladestationsplatte sorgt sie auch für eine glänzende Optik und unterstreicht das Design Ihres Roboterrasenmähers.</p>
      <p>Die Garage bietet Schutz vor <strong>Hagelkörnern, Regen und herabfallenden Ästen</strong>, auch die Gefahr von Blitzeinschlägen wird geringer (vor allem, wenn Roboter ungeschützt z.B. auf einer Wiese seinen Dienst versieht).</p>
      <p>Ab jetzt auch in der Premiumversion lieferbar.</p>
      <p><strong>Die Garage ist UV-unempfindlich und passt zu jedem Rasenroboter!</strong></p>
    </div>

    <aside class="versions">
      Die Box gibt es in zwei unterschiedlichen Ausführungen:
      <strong>Basic Version &amp; Expert Version</strong>
    </aside>

    <div class="backside-hint">
      <svg viewBox="0 0 14 12"><path d="M0 6h10M6 1.5l5 4.5-5 4.5" fill="none" stroke="#111" stroke-width="2"/></svg>
      <span>Informationen<br>auf der Rückseite!</span>
    </div>

    <p class="contact-cta">Kontaktieren Sie uns bei offenen Fragen, wir helfen Ihnen gerne weiter!</p>

    <footer class="contact-bar">Telefon: 0221 555012-0 • E-Mail: info@rasenhaus-box.de</footer>
  </main>
</body>
</html>
```